We need a business card for a company which is just starting up. The company name is Meridale Executive Services and we do a variety of things such as: support services for executives/leaders, sales team creation/management/training, and implementation of new programs to enhance a company's culture. The final design should be simple, professional and create a buzz of wanting to learn more. The owner is a woman of power, poise and leadership while she maintains qualities of caring, compassionate and honest. Her clients respect and refer her constantly. The colors are up for negotiation but should capture strength and softness at the same time. Possible colors: chocolate brown, dark pink, periwinkle. See attachment.

Target Market(s)

Medium to Large Businesses

Industry/Entity Type

Leadership

Requirements
Nice to have
• Qr code

```html
<!DOCTYPE html>
<html lang="en">
<head>
<meta charset="utf-8">
<title>Meridale Executive Services – Business Card</title>
<link rel="stylesheet" href="https://fonts.googleapis.com/css2?family=PT+Sans+Narrow:wght@400;700&display=swap">
<style>
  :root {
    --page: #ffffff;
    --chocolate-deep: #1c0a04;
    --chocolate: #3a1a0b;
    --chocolate-warm: #5a2a12;
    --tan: #c29a6b;
    --name-brown: #3d2410;
    --amber: #f6a93a;
    --white: #ffffff;
  }
  * { margin: 0; padding: 0; box-sizing: border-box; }
  html, body {
    width: 1200px;
    height: 904px;
    overflow: hidden;
    background: var(--page);
  }
  .canvas {
    position: relative;
    width: 1200px;
    height: 904px;
  }
  .card {
    position: absolute;
    width: 630px;
    height: 408px;
    overflow: hidden;
    background: var(--chocolate-deep);
  }
  .card--front { left: 37px; top: 31px; }
  .card--back  { left: 519px; top: 467px; }
  .card__texture {
    position: absolute;
    inset: 0;
    background:
      radial-gradient(ellipse 45% 35% at 30% 30%, rgba(110, 52, 22, 0.45), transparent 70%),
      radial-gradient(ellipse 40% 40% at 75% 60%, rgba(120, 58, 24, 0.40), transparent 70%),
      radial-gradient(ellipse 35% 30% at 20% 80%, rgba(100, 46, 18, 0.35), transparent 70%),
      radial-gradient(ellipse 30% 35% at 90% 15%, rgba(90, 40, 16, 0.30), transparent 70%),
      linear-gradient(160deg, var(--chocolate) 0%, var(--chocolate-deep) 55%, var(--chocolate) 100%);
  }
  .card__art {
    position: absolute;
    inset: 0;
    width: 100%;
    height: 100%;
  }
  .type {
    font-family: "PT Sans Narrow", "Arial Narrow", sans-serif;
  }
  .company-mark { fill: var(--white); font-weight: 700; font-size: 30px; }
  .name-band { fill: var(--tan); }
  .rule { stroke: var(--tan); stroke-width: 2; fill: none; }
  .person-name { fill: var(--name-brown); font-weight: 700; font-size: 40px; }
  .person-title { fill: var(--name-brown); font-weight: 400; font-size: 30px; }
  .contact-line { fill: var(--amber); font-weight: 400; font-size: 24px; }
  .back-company { fill: var(--amber); font-weight: 700; font-size: 46px; }
</style>
</head>
<body>
<main class="canvas">

  <section class="card card--front" aria-label="Business card front">
    <div class="card__texture" role="img" aria-label="Crumpled chocolate-brown paper texture"></div>
    <svg class="card__art" viewBox="0 0 672 435" xmlns="http://www.w3.org/2000/svg">
      <text class="type company-mark" x="23" y="55">Meridale Executive Services</text>

      <polygon class="name-band" points="0,270 336,173 365,285 0,389"/>
      <polyline class="rule" points="677,69 336,173 409,435"/>

      <g transform="rotate(-16 45 312)">
        <text class="type person-name" x="45" y="312">Renata Calloway</text>
      </g>
      <g transform="rotate(-16 59 355)">
        <text class="type person-title" x="59" y="355">Owner</text>
      </g>

      <g class="contact" transform="rotate(-18 362 199)">
        <text class="type contact-line" x="362" y="199">Phone (555) 555-5555</text>
        <text class="type contact-line" x="362" y="233">www.website.com</text>
        <text class="type contact-line" x="362" y="267">Email renata@email.com</text>
      </g>
    </svg>
  </section>

  <section class="card card--back" aria-label="Business card back">
    <div class="card__texture" role="img" aria-label="Crumpled chocolate-brown paper texture"></div>
    <svg class="card__art" viewBox="0 0 672 435" xmlns="http://www.w3.org/2000/svg">
      <text class="type back-company" x="336" y="219" text-anchor="middle">Meridale Executive Services</text>
    </svg>
  </section>

</main>
</body>
</html>
```